"Tovel" Health Drink: Bottle Label Design

My name's Dorian and I am starting a new health drink company in London, Ontario, Canada called "Tovel". I need a design for "only" the "front labelling" of one of my drinks. I have created a drink that tastes great and helps you live healthier at the same time! I currently attend The Harold Penwick School of Business and I am starting this company at the school years end. Im just starting out so if you can make a great design for me once I may need you again!

Our solution is simple; I'm providing drinks that are low calorie, low sugar, and nutritious to a market that has limited healthy drink options. With the brand name “Tovel” and the “Daily Balance” drink name, I hope to capture the 18-29 yr. old female demographic although we are doing so without alienating the male and older age demographics.

There are seven important aspects on the bottle. The most prominent is the Tovel brand name and logo. Tovel is written in eloquent writing with the dot on the “i” as a stevia leaf, the logo is half a person with a silhouette of a person adjacent to it resembling a mirror like figure, hence “Tovel”, and hence the company motto “Shape Your Day”.

Underneath the logo is the drink name “Daily Balance”. At the bottom of the drink I am presenting the drink as 50 calories/bottle along with a symbol of a stevia leaf with the words “stevia sweetened” adjacent to it and a "check mark" adjacent to that.

Finally, in a band around the top of the bottle, I will state the flavour. The flavours (ex. Dragon Fruit & Sweet Cherry) are a combination of both a super fruit and a traditional fruit.

The logo in the middle should be designed so that it is transferable to any other drink label or advertising. For this drink I would want a cherry red colour with all "stevia" leaves as green and the check mark green as well. The label is 142mm high and 63mm wide.

I have attached some files of what I think it should look like but I am totally open to variations! (Also, attached some pictures of the fruit and stevia if you don't know what they look like)

Thanks and I wish you best of luck!
Updates

I have made my project NON-REFUNDABLE, "QORVEX" currently has the best design! Hope to be seeing some competing designs! 

Industry/Entity Type

Health

```html
<!DOCTYPE html>
<html lang="en">
<head>
<meta charset="utf-8">
<title>Tovel Daily Balance – Front Label</title>
<link href="https://fonts.googleapis.com/css2?family=Oswald:wght@500;600&family=Playfair+Display:ital,wght@0,600;1,400&display=swap" rel="stylesheet">
<style>
  :root {
    --canvas: #ffffff;
    --label-edge: #8a8a8a;
    --leaf-green: #3aa845;
    --berry-pink: #e8318a;
    --sky-blue: #27a8e0;
    --badge-orange: #f39a2e;
    --volume-blue: #2a4a9a;
    --white: #ffffff;
  }
  * { margin: 0; padding: 0; box-sizing: border-box; }
  html, body {
    width: 1200px; height: 1178px; overflow: hidden;
    background: var(--canvas);
  }
  .label {
    position: absolute; left: 370px; top: 70px;
    width: 460px; height: 1038px;
    background: var(--white);
    border: 1.5px solid var(--label-edge);
    overflow: hidden;
  }
  .stevia-badge {
    position: absolute; left: 45px; top: 61px;
    width: 157px; height: 101px;
    border: 4px solid var(--leaf-green);
    color: var(--leaf-green);
    font-family: "Oswald", sans-serif; font-weight: 600;
    text-align: center; text-transform: uppercase;
    display: flex; flex-direction: column; justify-content: center;
    line-height: 1.05;
  }
  .stevia-badge .word-main { font-size: 34px; }
  .stevia-badge .word-sub { font-size: 21px; letter-spacing: 0.5px; }
  .leaf-photo {
    position: absolute; left: 210px; top: 0;
    width: 250px; height: 190px;
    background: radial-gradient(ellipse at 55% 40%, #4f9a3a 0%, #7cbf5a 45%, rgba(255,255,255,0) 72%);
  }
  .brand {
    position: absolute; left: 0; top: 198px; width: 460px;
    text-align: center;
  }
  .brand-name {
    font-family: "Playfair Display", serif; font-weight: 600;
    font-size: 104px; line-height: 1; color: var(--leaf-green);
    display: inline-flex; align-items: center; gap: 14px;
  }
  .brand-name .brand-dot {
    width: 18px; height: 18px; border-radius: 50%;
    background: var(--leaf-green);
  }
  .tagline {
    position: absolute; right: 48px; top: 308px;
    font-family: "Playfair Display", serif; font-style: italic;
    font-size: 31px; color: var(--leaf-green);
  }
  .flavour {
    position: absolute; left: 45px; top: 376px;
    font-family: "Oswald", sans-serif; font-weight: 500;
    text-transform: uppercase; font-size: 42px; line-height: 50px;
    color: var(--berry-pink);
  }
  .drink-name {
    position: absolute; left: 45px; top: 494px;
    font-family: "Oswald", sans-serif; font-weight: 500;
    text-transform: uppercase; font-size: 44px; line-height: 50px;
    color: var(--sky-blue); letter-spacing: 0.5px;
  }
  .fruit-photo {
    position: absolute; left: 0; top: 610px;
    width: 460px; height: 380px;
    background:
      radial-gradient(ellipse at 78% 40%, #f4f0f0 0%, #f4f0f0 28%, #e2468e 42%, rgba(255,255,255,0) 60%),
      radial-gradient(ellipse at 22% 35%, #f08cbc 0%, rgba(255,255,255,0) 45%),
      radial-gradient(ellipse at 38% 72%, #8a0f1c 0%, #b5142a 30%, rgba(255,255,255,0) 58%);
  }
  .calorie-badge {
    position: absolute; left: 72px; top: 544px;
    width: 108px; height: 108px; border-radius: 50%;
    background: var(--badge-orange); color: var(--white);
    font-family: "Oswald", sans-serif; font-weight: 600;
    text-align: center; text-transform: uppercase;
    display: flex; flex-direction: column; justify-content: center;
    line-height: 1;
  }
  .calorie-badge .count { font-size: 52px; }
  .calorie-badge .unit { font-size: 12px; margin-top: 2px; }
  .volume {
    position: absolute; left: 45px; top: 992px;
    font-family: "Oswald", sans-serif; font-weight: 500;
    font-size: 23px; color: var(--volume-blue);
  }
</style>
</head>
<body>
  <main class="label">
    <div class="leaf-photo" role="img" aria-label="Photo of fresh green stevia leaves"></div>
    <div class="stevia-badge">
      <span class="word-main">Stevia</span>
      <span class="word-sub">Swettened</span>
    </div>

    <div class="brand">
      <span class="brand-name">Tovel<span class="brand-dot"></span></span>
    </div>
    <p class="tagline">Shape Your Day.</p>

    <h1 class="flavour">Dragon Fruit<br>+ Sweet Cherry</h1>
    <h2 class="drink-name">Daily Balance</h2>

    <div class="fruit-photo" role="img" aria-label="Photo of halved dragon fruit with sweet cherries"></div>
    <div class="calorie-badge">
      <span class="count">25</span>
      <span class="unit">Calories<br>per serving</span>
    </div>

    <p class="volume">473 ml</p>
  </main>
</body>
</html>
```